Need simple and modern looking business card with all my information on one side and logo on the other side
Info :
Company name - VELTRIN CONSTRUCTION LLC
Company addres- 418 maple 307th. Dunford hill ny 10583
Email- veltrinllc@pormail.Com
Company phone number 555-318-4096
Cell number- 555-762-0384
Web site - veltrinllc.Com
My name Gerald haverstrom

Target Market(s)

Construction , home improvement, remodeling

Industry/Entity Type

Construction

Contact Information for Business Card

It has to be moder but at the same time simple

Font styles to use
Sans Serif

Colors
0255a3
ffffff
000000
f78f20
b1b1b1
9d9d9d
1b1b1b
33a6d7
ec1f27

Requirements
Must have
• My logo on one side maybe with a some kind of background on the other side all my information
Nice to have
• Some kind of background pictures provided by you .PLEASE HAVE ACCOUNT WITH PIXVALEMOR WILL NOT PAY ANY EXTRA FEES .
Should not have
• Any kind of hamer, nails,screws, helmets itp. Please do not copy the other designs come up with something new.

```html
<!DOCTYPE html>
<html lang="en">
<head>
<meta charset="utf-8">
<title>Veltrin Construction LLC — Business Card</title>
<link rel="stylesheet" href="https://fonts.googleapis.com/css2?family=Open+Sans:wght@400;600;700&display=swap">
<style>
  :root {
    --orange: #f78f20;
    --orange-deep: #d97a12;
    --olive: #8a6a1e;
    --black: #000000;
    --ink: #1b1b1b;
    --white: #ffffff;
    --stage: #e9e9e9;
  }
  * { box-sizing: border-box; margin: 0; padding: 0; }
  html, body {
    width: 1200px; height: 1200px; overflow: hidden;
    background: var(--stage);
    font-family: "Open Sans", Arial, sans-serif;
  }
  .canvas { position: relative; width: 1200px; height: 1200px; }

  .card {
    position: absolute; left: 220px; width: 760px; height: 434px;
    overflow: hidden;
    box-shadow: 0 6px 18px rgba(0,0,0,.18);
  }

  /* Logo side */
  .card--front { top: 110px; }
  .front-backdrop {
    position: absolute; inset: 0;
    background:
      radial-gradient(ellipse 38% 45% at 22% 45%, rgba(120,95,30,.55), transparent 70%),
      radial-gradient(ellipse 30% 40% at 80% 70%, rgba(120,95,30,.45), transparent 70%),
      radial-gradient(ellipse 25% 30% at 60% 20%, rgba(255,190,90,.5), transparent 70%),
      linear-gradient(135deg, var(--orange) 0%, var(--orange-deep) 55%, var(--orange) 100%);
  }
  .front-brand {
    position: absolute; left: 0; right: 0; top: 50%;
    transform: translateY(-50%);
    display: flex; align-items: center; justify-content: center; gap: 18px;
    color: var(--white); font-weight: 700; font-size: 40px; letter-spacing: 2px;
  }
  .front-brand .mark { width: 34px; height: 34px; background: var(--white); }

  /* Info side */
  .card--back { top: 656px; background: var(--white); }
  .back-brand {
    position: absolute; left: 46px; top: 70px;
    display: flex; align-items: center; gap: 12px;
    color: var(--black); font-weight: 700; font-size: 25px; letter-spacing: 1px;
  }
  .back-brand .mark { width: 22px; height: 22px; background: var(--orange); }

  .person { position: absolute; right: 90px; top: 104px; text-align: right; }
  .person__name { color: var(--orange); font-weight: 700; font-size: 23px; letter-spacing: .5px; }
  .person__role { color: var(--ink); font-size: 15px; margin-top: 4px; letter-spacing: .5px; }

  .edge-chevron { position: absolute; right: 0; top: 148px; }

  .address { position: absolute; left: 46px; top: 232px; color: var(--ink); font-size: 16px; line-height: 22px; }
  .address__company { color: var(--orange); font-weight: 700; font-size: 15px; }

  .contacts { position: absolute; left: 430px; top: 270px; list-style: none; color: var(--ink); font-size: 16px; }
  .contacts li { display: flex; align-items: center; gap: 10px; height: 24px; }
  .contacts svg { flex: none; }

  .footer-band { position: absolute; left: 0; bottom: 0; }
  .website {
    position: absolute; right: 150px; bottom: 10px;
    color: var(--ink); font-size: 16px;
  }
</style>
</head>
<body>
<main class="canvas">

  <section class="card card--front" aria-label="Business card logo side">
    <div class="front-backdrop" role="img" aria-label="Blurred orange background of floating cubes"></div>
    <div class="front-brand"><span class="mark"></span>VELTRIN CONSTRUCTION LLC</div>
  </section>

  <section class="card card--back" aria-label="Business card information side">
    <div class="back-brand"><span class="mark"></span>VELTRIN CONSTRUCTION LLC</div>

    <div class="person">
      <p class="person__name">GERALD HAVERSTROM</p>
      <p class="person__role">MANAGING DIRECTOR</p>
    </div>

    <svg class="edge-chevron" width="70" height="70" viewBox="0 0 70 70" aria-hidden="true">
      <polyline points="70,4 18,35 70,66" fill="none" stroke="var(--orange)" stroke-width="9"/>
    </svg>

    <div class="address">
      <p class="address__company">VELTRIN CONSTRUCTION LLC</p>
      <p>418 maple 307th.</p>
      <p>Dunford hill ny 10583</p>
    </div>

    <ul class="contacts">
      <li>
        <svg width="16" height="16" viewBox="0 0 16 16" aria-hidden="true"><rect width="16" height="16" rx="2" fill="var(--orange)"/><path d="M5 3.5l2 2-1 1.2c.6 1.3 1.6 2.3 2.8 2.8L10 8.5l2 2-1.3 1.6C7.4 11.8 4.2 8.6 3.9 5z" fill="var(--white)"/></svg>
        555-318-4096
      </li>
      <li>
        <svg width="16" height="16" viewBox="0 0 16 16" aria-hidden="true"><rect width="16" height="16" rx="2" fill="var(--orange)"/><rect x="5" y="2.5" width="6" height="11" rx="1" fill="var(--white)"/><rect x="6" y="4" width="4" height="7" fill="var(--orange)"/></svg>
        555-762-0384
      </li>
      <li>
        <svg width="16" height="16" viewBox="0 0 16 16" aria-hidden="true"><rect width="16" height="16" rx="2" fill="var(--orange)"/><rect x="3" y="4.5" width="10" height="7" fill="var(--white)"/><polyline points="3,4.5 8,8.5 13,4.5" fill="none" stroke="var(--orange)" stroke-width="1.2"/></svg>
        veltrinllc@pormail.Com
      </li>
    </ul>

    <svg class="footer-band" width="760" height="46" viewBox="0 0 760 46" aria-hidden="true">
      <polygon points="0,14 380,14 350,46 0,46" fill="var(--black)"/>
      <polygon points="395,0 760,0 760,46 350,46" fill="var(--orange)"/>
    </svg>
    <p class="website">veltrinllc.Com</p>
  </section>

</main>
</body>
</html>
```